Upmarket building and construction company needs signage

Our building company R Brent Construction, needs signage to put up on the side of our vehicle trailers and on site fencing. We are a building company that specialises in residential construction and carpentry .

I will attach our logo and some inspirational pics for site fencing as well as what our trailer looks like .
Other details i would like on the sign are our
( email) rbrentconstruction@mailbox-example.net
(mobile ) 0493 518 264
(website ) rbrentconstruction. example.net

Target Market(s)

Home owners looking for a reliable local builder who produces good quality work. I have attached some inspirational pics.

Industry/Entity Type

Building and Construction

Colors

Designer to choose colors to be used in the design.

Requirements
Must have
• Our logo, contact information
Nice to have
• We would like the design to have elements of being Elegant, Serious, Modern, Professional, Masculine, Conservative and Upmarket.

```html
<!DOCTYPE html>
<html lang="en">
<head>
<meta charset="utf-8">
<title>R Brent Construction – Site Signage</title>
<link rel="stylesheet" href="https://fonts.googleapis.com/css2?family=Jost:ital,wght@0,300;0,400;0,700;1,500&display=swap">
<style>
  :root {
    --backdrop: #5a5a5a;
    --sign-white: #ffffff;
    --plan-tint: #faf6ef;
    --ink-grey: #6d6c6e;
    --gold: #b07824;
    --charcoal: #424242;
    --text-light: #ffffff;
  }
  html, body {
    margin: 0;
    padding: 0;
    width: 1200px;
    height: 986px;
    overflow: hidden;
    background: var(--backdrop);
  }
  .sign {
    position: absolute;
    left: 40px;
    top: 82px;
    width: 1120px;
    height: 821px;
    display: block;
    font-family: "Jost", "Futura", sans-serif;
  }
  .sign__base { fill: var(--sign-white); }
  .sign__plan-area { fill: url(#planTint); }
  .sign__gold-band { fill: var(--gold); }
  .sign__dark-panel { fill: var(--charcoal); }
  .brand-name { fill: var(--ink-grey); font-weight: 300; }
  .brand-tagline { fill: var(--ink-grey); font-weight: 400; }
  .services { fill: var(--text-light); font-style: italic; font-weight: 500; }
  .phone { fill: var(--text-light); font-weight: 700; }
  .divider { fill: var(--gold); }
  .contact-line { fill: var(--text-light); font-weight: 400; font-size: 22px; }
  .contact-icon { fill: none; stroke: var(--text-light); stroke-width: 1.6; }
</style>
</head>
<body>
<svg class="sign" viewBox="0 0 1120 821" xmlns="http://www.w3.org/2000/svg" aria-label="R Brent Construction sign">
  <defs>
    <linearGradient id="planTint" x1="0" y1="0" x2="0" y2="1">
      <stop offset="0" stop-color="#fdfbf7"/>
      <stop offset="1" stop-color="#faf6ef"/>
    </linearGradient>
  </defs>

  <rect class="sign__base" x="0" y="0" width="1120" height="821"/>
  <rect class="sign__plan-area" x="0" y="0" width="1120" height="600" role="img"
        aria-label="Faint architectural elevation drawing of a house in the background"/>

  <path class="sign__gold-band" d="M0 436 Q560 753 1120 436 L1120 821 L0 821 Z"/>
  <path class="sign__dark-panel" d="M0 491 Q560 746 1120 491 L1120 821 L0 821 Z"/>

  <g class="brand">
    <text class="brand-name" x="281" y="384" font-size="160" textLength="558" lengthAdjust="spacing">R BRENT</text>
    <text class="brand-name" x="281" y="467" font-size="66" textLength="558" lengthAdjust="spacing">CONSTRUCTION</text>
    <text class="brand-tagline" x="281" y="526" font-size="43" textLength="558" lengthAdjust="spacing">BUILDING AND CARPENTRY</text>
  </g>

  <text class="services" x="194" y="680" font-size="31" textLength="731" lengthAdjust="spacingAndGlyphs">NEW BUILDS I RENOVATIONS I RESIDENTIAL I COMMERCIAL</text>

  <text class="phone" x="70" y="779" font-size="76" textLength="493" lengthAdjust="spacing">0493 518 264</text>
  <rect class="divider" x="588" y="722" width="9" height="57"/>

  <g class="contact">
    <g class="contact-icon" transform="translate(642 727)">
      <circle cx="0" cy="0" r="11"/>
      <ellipse cx="0" cy="0" rx="5" ry="11"/>
      <line x1="-11" y1="0" x2="11" y2="0"/>
    </g>
    <text class="contact-line" x="662" y="735">rbrentconstruction. example.net</text>

    <g class="contact-icon" transform="translate(642 768)">
      <rect x="-11" y="-8" width="22" height="16"/>
      <polyline points="-11,-8 0,2 11,-8"/>
    </g>
    <text class="contact-line" x="662" y="776">rbrentconstruction@mailbox-example.net</text>
  </g>
</svg>
</body>
</html>
```